Tidewell Claimworks Website - a medical billing website - one page

I need a one-page website to attract potential clients to my medical billing services - I am in the process of creating a logo, the contest ends Friday. I also have some ideas and am writing some of the copy that I can send you.

SLOGAN: We Turn Codes Into Money

MISSION STATEMENT: Give compassionate quality service and precision medical billing with urgency

Target Market(s)

MD's, physical therapists, occupational therapists, speech therapists, chiropractors, psychologists, psychiatrists, dentists and new grads of the above

Coding

Coded - Design and coding required

Number of Pages Required

1 page

Font styles to use
Sans Serif
Decorative
Script

Colors
33a6d7
add136
87cfc6
cadf82
9bcb3c
85cae6

Requirements
Must have
• I am working on the major points of copy that I need, plus
• ranking search terms keywords and phrases
Nice to have
• creativity to draw clients in
• my color choices below are similar to the logo coloring - but if you like something different feel free to use your own creative colors.

```html
<!DOCTYPE html>
<html lang="en">
<head>
<meta charset="utf-8">
<title>Tidewell Claimworks — Medical Billing</title>
<link href="https://fonts.googleapis.com/css2?family=IBM+Plex+Sans:wght@400;600;700&family=Open+Sans:wght@400;600;700&display=swap" rel="stylesheet">
<style>
:root{
  --blue:#33a6d7;
  --blue-deep:#2a6f98;
  --green:#9bcb3c;
  --green-logo:#3f8a3a;
  --ink:#333;
  --muted:#777;
  --line:#ddd;
  --footer:#2a5d84;
  --white:#fff;
  --shade:rgba(0,0,0,.74);
  --close:#9bcb3c;
}
*{margin:0;padding:0;box-sizing:border-box}
html,body{width:1200px;height:3938px;overflow:hidden}
body{font-family:"Open Sans",Arial,sans-serif;color:var(--ink);background:#fff;position:relative}
.page{position:absolute;inset:0}
.abs{position:absolute}
.display{font-family:"IBM Plex Sans","Open Sans",sans-serif}

/* header */
.site-header{top:0;left:0;width:1200px;height:107px;background:var(--white)}
.brand{left:135px;top:24px;display:flex;align-items:center;gap:14px}
.brand-mark{width:58px;height:58px;background:var(--green-logo)}
.brand-name{font-family:"IBM Plex Sans",sans-serif;font-weight:700;font-size:23px;line-height:27px;color:var(--green-logo);letter-spacing:.5px}
.contact-chip{display:flex;align-items:center;gap:10px}
.chip-icon{width:26px;height:26px;border-radius:50%;background:var(--blue);display:flex;align-items:center;justify-content:center}
.chip-label{font-size:10px;color:var(--muted);text-transform:uppercase;line-height:12px}
.chip-value{font-size:16px;color:#555;line-height:20px}
.main-nav{top:72px;left:532px;display:flex;gap:0}
.main-nav a{font-size:12px;font-weight:600;color:#555;text-decoration:none;padding:4px 10px;margin-right:11px;letter-spacing:.3px}
.main-nav a.active{background:var(--blue);color:#fff}

/* hero */
.hero{top:107px;left:0;width:1200px;height:553px;background:linear-gradient(110deg,#7a6a58 0%,#b7a997 35%,#d8d2c8 60%,#8f877c 100%)}
.hero-title{left:131px;top:300px;font-size:50px;line-height:56px;font-weight:700;color:#fff;letter-spacing:1px}
.hero-sub{left:134px;top:418px;font-size:21px;color:#fff}
.btn{display:inline-block;font-size:13px;font-weight:700;text-transform:uppercase;color:#fff;letter-spacing:.5px;text-align:center}
.btn-green{background:var(--green)}
.hero .btn{left:138px;top:473px;width:111px;height:29px;line-height:29px}
.dots{left:550px;top:511px;display:flex;gap:13px;align-items:center}
.dots span{width:9px;height:9px;border-radius:50%;background:#fff}
.dots span.on{width:13px;height:13px;background:transparent;border:2px solid #fff}

/* services */
.section-title{width:1200px;left:0;text-align:center;font-family:"IBM Plex Sans",sans-serif;font-weight:600;font-size:25px;color:#333;letter-spacing:.5px}
.section-rule{left:566px;width:68px;height:2px;background:#333}
.service{width:200px;text-align:center}
.service svg{display:block;margin:0 auto}
.service h3{margin-top:34px;font-size:13px;font-weight:700;color:#333;letter-spacing:.3px}
.service p{margin-top:10px;font-size:12px;line-height:17px;color:var(--muted);padding:0 10px}

/* welcome */
.welcome{top:1335px;left:0;width:1200px;height:511px;background:linear-gradient(120deg,#e6eef2,#c9d9e2 50%,#eef2f4)}
.welcome-panel{top:0;left:0;width:543px;height:511px;background:var(--blue)}
.welcome-kicker{left:133px;top:62px;font-size:21px;color:#fff;font-weight:600}
.welcome-title{left:133px;top:90px;font-size:31px;color:#fff;font-weight:700}
.welcome-rule{left:133px;top:140px;width:73px;height:2px;background:#fff}
.welcome-copy{left:133px;top:178px;width:335px;font-size:15px;line-height:22.3px;color:#fff}
.welcome .btn{left:133px;top:417px;width:114px;height:31px;line-height:31px}

/* benefits */
.benefits{top:1846px;left:0;width:1200px;height:532px;background:#f5f5f5}
.benefits-media{top:0;left:0;width:720px;height:532px;background:linear-gradient(130deg,#f2f2f2,#dcdcdc 55%,#f4f4f4)}
.benefits-title{left:742px;top:50px;font-size:25px;font-weight:600;color:#2e6f92}
.benefit{left:742px;display:flex;align-items:center;gap:24px}
.benefit-icon{width:56px;height:56px;border-radius:50%;border:2px solid #666;display:flex;align-items:center;justify-content:center}
.benefit-text{font-size:18px;line-height:26px;color:#555;width:220px}

/* cta band */
.cta{top:2378px;left:0;width:1200px;height:156px;background:var(--green)}
.cta-text{left:133px;top:54px;font-size:25px;line-height:33px;font-weight:700;color:#fff;letter-spacing:.8px}
.cta .btn{left:898px;top:52px;width:169px;height:49px;line-height:49px;background:var(--blue);font-size:17px;font-weight:600}

/* resources */
.card{width:292px;height:370px;background:#fff;border:1px solid #e6e6e6}
.card-media{width:100%;height:173px;background:linear-gradient(135deg,#e9eef0,#c6d0d5)}
.card h4{margin:32px 30px 0;font-size:13.5px;line-height:21px;font-weight:700;color:#333;letter-spacing:.3px}
.card p{margin:10px 30px 0;font-size:11.5px;line-height:17px;color:var(--muted)}
.card .btn{margin:14px 0 0 30px;width:95px;height:27px;line-height:27px;font-size:11px}

/* solutions */
.solutions{top:3111px;left:0;width:1200px;height:426px;background:linear-gradient(100deg,#e8e8e6,#f6f6f4 45%,#d8dadb)}
.solutions h2{top:58px;width:1200px;text-align:center;font-family:"IBM Plex Sans",sans-serif;font-weight:600;font-size:28px;color:#333}
.solutions .lines{top:112px;width:1200px;text-align:center;font-size:13.5px;line-height:26px;color:#555}
.solutions .btn{left:546px;top:192px;width:108px;height:30px;line-height:30px}

/* footer */
.site-footer{top:3537px;left:0;width:1200px;height:401px;background:var(--footer);color:#fff}
.site-footer .brand{left:135px;top:121px}
.site-footer .brand-mark{background:#fff;opacity:.9}
.site-footer .brand-name{color:#fff}
.foot-head{font-size:14px;font-weight:700;letter-spacing:.5px;color:#dfe9f0}
.foot-menu a{display:block;font-size:13px;line-height:24px;color:#dfe9f0;text-decoration:none}
.foot-item{display:flex;align-items:center;gap:14px;font-size:12.5px;line-height:17px;color:#dfe9f0}
.foot-icon{width:28px;height:28px;border-radius:50%;background:#fff;opacity:.9;display:flex;align-items:center;justify-content:center;flex:none}
.copyright{top:356px;width:1200px;text-align:center;font-size:11px;color:#cbd9e3}

/* promo modal */
.shade{inset:0;background:var(--shade)}
.promo{left:310px;top:162px;width:606px;height:292px;background:#fff;text-align:center}
.promo-close{position:absolute;right:16px;top:16px}
.promo h2{margin-top:72px;font-family:"Open Sans",sans-serif;font-weight:700;font-size:29px;line-height:40px;color:#111}
.promo .btn{margin-top:19px;background:var(--blue);width:176px;height:32px;line-height:32px;font-size:16px}
</style>
</head>
<body>
<div class="page">

  <header class="site-header abs">
    <div class="brand abs"><div class="brand-mark"></div><div class="brand-name">TIDEWELL<br>CLAIMWORKS</div></div>
    <div class="contact-chip abs" style="left:660px;top:24px">
      <div class="chip-icon"><svg width="14" height="10" viewBox="0 0 14 10"><rect x="0.5" y="0.5" width="13" height="9" fill="none" stroke="#fff"/><path d="M1 1l6 5 6-5" fill="none" stroke="#fff"/></svg></div>
      <div><div class="chip-label">E-mail us</div><div class="chip-value">hello@tidewellclaimworks.com</div></div>
    </div>
    <div class="contact-chip abs" style="left:925px;top:24px">
      <div class="chip-icon"><svg width="14" height="14" viewBox="0 0 14 14"><path d="M3 1l3 3-2 2c1 2 2 3 4 4l2-2 3 3-2 2C6 13 1 8 1 3z" fill="#fff"/></svg></div>
      <div><div class="chip-label">Call us</div><div class="chip-value">555.014.2290</div></div>
    </div>
    <nav class="main-nav abs">
      <a class="active" href="#">HOME</a><a href="#">ABOUT US</a><a href="#">SERVICES</a><a href="#">BENEFITS</a><a href="#">RESOURCES</a><a href="#">CONTACT US</a>
    </nav>
  </header>

  <section class="hero abs" role="img" aria-label="Photo of hands typing on a laptop showing an invoice">
    <h1 class="hero-title abs display">BILLING<br>SERVICES</h1>
    <p class="hero-sub abs">Lorem Ipsum is simply dummy text</p>
    <span class="btn btn-green abs">Read more</span>
    <div class="dots abs"><span></span><span></span><span class="on"></span><span></span><span></span></div>
  </section>

  <section class="services">
    <h2 class="section-title abs" style="top:700px">OUR SERVICES</h2>
    <div class="section-rule abs" style="top:745px"></div>

    <div class="service abs" style="left:128px;top:818px">
      <svg width="56" height="68" viewBox="0 0 56 68" fill="none" stroke="#2a6f98" stroke-width="3"><rect x="4" y="8" width="48" height="58" rx="3"/><rect x="18" y="2" width="20" height="10"/><path d="M28 20l3 6 6 1-4 4 1 6-6-3-6 3 1-6-4-4 6-1z"/><path d="M14 46h28M14 54h28"/></svg>
      <h3>CODING REVIEW</h3><p>Lorem Ipsum is simply dummy text of the printing and type setting industry</p>
    </div>
    <div class="service abs" style="left:374px;top:818px">
      <svg width="72" height="68" viewBox="0 0 72 68" fill="none" stroke="#2a6f98" stroke-width="3"><circle cx="14" cy="26" r="8"/><circle cx="18" cy="52" r="8"/><path d="M20 30l30-20M24 48l26-12"/><rect x="38" y="14" width="26" height="40" transform="rotate(30 51 34)"/></svg>
      <h3>COST REDUCTION</h3><p>Lorem Ipsum is simply dummy text of the printing and type setting industry</p>
    </div>
    <div class="service abs" style="left:620px;top:818px">
      <svg width="72" height="68" viewBox="0 0 72 68"><ellipse cx="36" cy="40" rx="28" ry="22" fill="#2a6f98"/><rect x="18" y="56" width="8" height="10" fill="#2a6f98"/><rect x="44" y="56" width="8" height="10" fill="#2a6f98"/><circle cx="36" cy="10" r="7" fill="#2a6f98"/></svg>
      <h3>SAVE MONEY</h3><p>Lorem Ipsum is simply dummy text of the printing and type setting industry</p>
    </div>
    <div class="service abs" style="left:872px;top:818px">
      <svg width="56" height="68" viewBox="0 0 56 68"><rect x="4" y="2" width="48" height="64" rx="4" fill="#2a6f98"/><path d="M14 14h28M14 24h28M14 34h28M14 44h28M14 54h20" stroke="#fff" stroke-width="3"/></svg>
      <h3>BILLING SOPHISTICATION</h3><p>Lorem Ipsum is simply dummy text of the printing and type setting industry</p>
    </div>

    <div class="service abs" style="left:128px;top:1078px">
      <svg width="72" height="68" viewBox="0 0 72 68" fill="none" stroke="#2a6f98" stroke-width="3"><path d="M14 14a30 30 0 0 0 44 44M58 14a30 30 0 0 1-4 40"/><path d="M36 18l5 10 11 1-8 7 3 11-11-6-11 6 3-11-8-7 11-1z" fill="#2a6f98"/></svg>
      <h3>REVIEW &amp; FOLLOW UP</h3><p>Lorem Ipsum is simply dummy text of the printing and type setting industry</p>
    </div>
    <div class="service abs" style="left:374px;top:1078px">
      <svg width="64" height="68" viewBox="0 0 64 68" fill="none" stroke="#2a6f98" stroke-width="3"><rect x="4" y="28" width="56" height="36"/><rect x="12" y="4" width="40" height="40"/><path d="M22 36V20M30 36V14M38 36V24M46 36V18"/></svg>
      <h3>REPORTING</h3><p>Lorem Ipsum is simply dummy text of the printing and type setting industry</p>
    </div>
    <div class="service abs" style="left:620px;top:1078px">
      <svg width="64" height="68" viewBox="0 0 64 68" fill="none" stroke="#2a6f98" stroke-width="3"><path d="M6 4h30l12 12v48H6z"/><path d="M14 24h22M14 32h22M14 40h14"/><circle cx="46" cy="50" r="12"/><path d="M40 50l4 4 8-8"/></svg>
      <h3>CONTRACTING</h3><p>Lorem Ipsum is simply dummy text of the printing and type setting industry</p>
    </div>
    <div class="service abs" style="left:872px;top:1078px">
      <svg width="68" height="68" viewBox="0 0 68 68"><circle cx="34" cy="32" r="30" fill="#2a6f98"/><path d="M10 60l10-10" stroke="#2a6f98" stroke-width="8"/><path d="M20 24h28M20 34h28M20 44h18" stroke="#fff" stroke-width="4"/></svg>
      <h3>PATIENT COMMUNICATION</h3><p>Lorem Ipsum is simply dummy text of the printing and type setting industry</p>
    </div>
  </section>

  <section class="welcome abs" role="img" aria-label="Photo of a doctor writing on a clipboard at a desk">
    <div class="welcome-panel abs"></div>
    <p class="welcome-kicker abs display">WELCOME TO</p>
    <h2 class="welcome-title abs display">TIDEWELL CLAIMWORKS</h2>
    <div class="welcome-rule abs"></div>
    <p class="welcome-copy abs">Medical billing services are companies that have the staff or department to handle patient billing and insurance issues for a medical practice. The job of a medical biller is to represent you and negotiate on your behalf to make sure you get paid for the medical services you provide. We communicate with the patient and their insurance company for every medical claim.</p>
    <span class="btn btn-green abs">Read more</span>
  </section>

  <section class="benefits abs">
    <div class="benefits-media abs" role="img" aria-label="Photo of a stethoscope resting on a billing statement with a calculator"></div>
    <h2 class="benefits-title abs display">BENEFITS</h2>
    <div class="benefit abs" style="top:121px"><div class="benefit-icon"><svg width="26" height="26" viewBox="0 0 26 26" fill="none" stroke="#666" stroke-width="2"><ellipse cx="13" cy="8" rx="9" ry="4"/><path d="M4 8v10c0 2 4 4 9 4s9-2 9-4V8M4 13c0 2 4 4 9 4s9-2 9-4"/></svg></div><div class="benefit-text">Simplifying financial record-keeping</div></div>
    <div class="benefit abs" style="top:201px"><div class="benefit-icon"><svg width="24" height="26" viewBox="0 0 24 26"><path d="M12 1L2 5v7c0 7 5 11 10 13 5-2 10-6 10-13V5z" fill="#666"/></svg></div><div class="benefit-text">Data protection for sensitive files</div></div>
    <div class="benefit abs" style="top:274px"><div class="benefit-icon"><svg width="26" height="24" viewBox="0 0 26 24" fill="none" stroke="#666" stroke-width="2"><path d="M2 22h22M6 20V12M11 20V6M16 20V10M21 20V4"/></svg></div><div class="benefit-text">High accuracy</div></div>
    <div class="benefit abs" style="top:343px"><div class="benefit-icon"><svg width="24" height="26" viewBox="0 0 24 26" fill="none" stroke="#666" stroke-width="2"><circle cx="12" cy="15" r="9"/><path d="M12 15V10M9 3h6M12 3v3"/></svg></div><div class="benefit-text">Quick turnaround time for insurance claims</div></div>
    <div class="benefit abs" style="top:423px"><div class="benefit-icon"><svg width="24" height="24" viewBox="0 0 24 24" fill="none" stroke="#666" stroke-width="2"><path d="M3 9V3h6M21 9V3h-6M3 15v6h6M21 15v6h-6M3 3l6 6M21 3l-6 6M3 21l6-6M21 21l-6-6"/></svg></div><div class="benefit-text">Scalability</div></div>
  </section>

  <section class="cta abs">
    <p class="cta-text abs display">SAVE MORE AND WORRY LESS<br>WITH RIGHT MEDICAL BILLING</p>
    <span class="btn abs">CONTACT US</span>
  </section>

  <section class="resources">
    <h2 class="section-title abs" style="top:2580px">RESOURCES</h2>
    <div class="section-rule abs" style="top:2628px"></div>
    <article class="card abs" style="left:133px;top:2680px"><div class="card-media" role="img" aria-label="Photo of a tablet showing a chart"></div><h4>LOREM IPSUM IS SIMPLY DUM MYTEXT OF THE PRINTIN</h4><p>Lorem Ipsum is simply dummy text of the printing and type setting industry ormal distribution of letters.</p><span class="btn btn-green">Read more</span></article>
    <article class="card abs" style="left:454px;top:2680px"><div class="card-media" role="img" aria-label="Photo of hands using a calculator"></div><h4>LOREM IPSUM IS SIMPLY DUM MYTEXT OF THE PRINTIN</h4><p>Lorem Ipsum is simply dummy text of the printing and type setting industry ormal distribution of letters.</p><span class="btn btn-green">Read more</span></article>
    <article class="card abs" style="left:775px;top:2680px"><div class="card-media" role="img" aria-label="Photo of a person writing notes on paperwork"></div><h4>LOREM IPSUM IS SIMPLY DUM MYTEXT OF THE PRINTIN</h4><p>Lorem Ipsum is simply dummy text of the printing and type setting industry ormal distribution of letters.</p><span class="btn btn-green">Read more</span></article>
  </section>

  <section class="solutions abs" role="img" aria-label="Photo of a desk with a laptop and a stethoscope">
    <h2 class="abs">WE DO SMART SOLUTIONS</h2>
    <p class="lines abs">PHYSICAL THERAPISTS &nbsp;|&nbsp; OCCUPATIONAL THERAPISTS &nbsp;|&nbsp; SPEECH THERAPISTS<br>CHIROPRACTORS &nbsp;|&nbsp; PSYCHOLOGISTS &nbsp;|&nbsp; PSYCHIATRISTS &nbsp;|&nbsp; DENTISTS</p>
    <span class="btn btn-green abs">Read more</span>
  </section>

  <footer class="site-footer abs">
    <div class="brand abs"><div class="brand-mark"></div><div class="brand-name">TIDEWELL<br>CLAIMWORKS</div></div>
    <div class="abs" style="left:434px;top:56px"><p class="foot-head">MENU</p>
      <nav class="foot-menu" style="margin-top:18px"><a href="#">HOME</a><a href="#">ABOUT US</a><a href="#">SERVICES</a><a href="#">BENEFITS</a><a href="#">RESOURCES</a><a href="#">CONTACT US</a></nav></div>
    <div class="abs" style="left:612px;top:56px"><p class="foot-head">CONTACT US</p>
      <div class="foot-item" style="margin-top:28px"><div class="foot-icon"><svg width="12" height="14" viewBox="0 0 12 14"><path d="M6 0a5 5 0 0 0-5 5c0 4 5 9 5 9s5-5 5-9a5 5 0 0 0-5-5z" fill="#2a5d84"/></svg></div><span>4410 Harbor Lane Avenue<br>Porthaven, CA 90210</span></div>
      <div class="foot-item" style="margin-top:26px"><div class="foot-icon"><svg width="12" height="12" viewBox="0 0 14 14"><path d="M3 1l3 3-2 2c1 2 2 3 4 4l2-2 3 3-2 2C6 13 1 8 1 3z" fill="#2a5d84"/></svg></div><span>Call us<br>555.014.2290</span></div>
      <div class="foot-item" style="margin-top:26px"><div class="foot-icon"><svg width="13" height="9" viewBox="0 0 14 10"><rect x="0.5" y="0.5" width="13" height="9" fill="none" stroke="#2a5d84"/><path d="M1 1l6 5 6-5" fill="none" stroke="#2a5d84"/></svg></div><span>Email us<br>hello@tidewellclaimworks.com</span></div>
    </div>
    <div class="abs" style="left:898px;top:56px"><p class="foot-head">FOLLOW US</p>
      <div class="foot-item" style="margin-top:28px"><div class="foot-icon"></div><span>Like us on<br>SOCIALNET</span></div>
      <div class="foot-item" style="margin-top:26px"><div class="foot-icon"></div><span>Follow us on<br>CHIRPLINE</span></div>
      <div class="foot-item" style="margin-top:26px"><div class="foot-icon"></div><span>Connect on<br>WORKLINK</span></div>
    </div>
    <p class="copyright abs">Copyright © 2016 All rights reserved</p>
  </footer>

  <div class="shade abs"></div>

  <aside class="promo abs" aria-label="Free first month offer">
    <svg class="promo-close" width="20" height="20" viewBox="0 0 20 20"><path d="M3 3l14 14M17 3L3 17" stroke="var(--close)" stroke-width="4" stroke-linecap="round"/></svg>
    <h2>GET YOUR 1 ST 30 DAYS<br>OF BILLING FOR FREE</h2>
    <span class="btn">NO OBLIGATIONS</span>
  </aside>

</div>
</body>
</html>
```